Business card for STEADYWAVE

Please design professional business card for IT consulting firm STEADYWAVE INC.
Use logo attached.
Use information from sample qNode business card attached.
replace qnode inc with STEADYWAVE INC.
as well as qnodeinc.com with steadywave.example

```html
<!DOCTYPE html>
<html lang="en">
<head>
<meta charset="utf-8">
<title>STEADYWAVE — Business Card</title>
<link rel="stylesheet" href="https://fonts.googleapis.com/css2?family=Poppins:wght@400;500;600&display=swap">
<style>
  :root {
    --stage-bg: #b4b4b4;
    --card-bg: #ffffff;
    --ink: #1c1c22;
    --accent-orange: #e9a043;
    --band-lilac: #e7dbec;
    --band-mist: #e6eef0;
    --band-sky: #d5f1fb;
    --band-peach: #fbe3c8;
    --rule-green: #7fd6b4;
    --rule-purple: #6a3aa0;
    --rule-blue: #5ec8ea;
    --rule-orange: #f07a1a;
  }
  * { box-sizing: border-box; margin: 0; padding: 0; }
  html, body { width: 1200px; height: 910px; overflow: hidden; }
  body {
    background: var(--stage-bg);
    font-family: "Poppins", sans-serif;
    color: var(--ink);
    position: relative;
  }
  .card {
    position: absolute;
    left: 50px; top: 165px;
    width: 1100px; height: 580px;
    background: var(--card-bg);
    border-radius: 58px;
    overflow: hidden;
  }
  .brand {
    position: absolute;
    left: 72px; top: 58px;
    display: flex; align-items: center; gap: 14px;
  }
  .brand-name {
    font-weight: 600;
    font-size: 66px;
    letter-spacing: 6px;
    line-height: 1;
    color: var(--ink);
  }
  .brand-mark {
    width: 26px; height: 26px;
    background: var(--accent-orange);
  }
  .job-title {
    position: absolute;
    left: 74px; top: 148px;
    font-size: 38px;
    font-weight: 400;
    color: var(--accent-orange);
    line-height: 1;
  }
  .info-band {
    position: absolute;
    left: 0; top: 224px;
    width: 100%; height: 303px;
    background:
      radial-gradient(ellipse 260px 160px at 52% 100%, var(--band-peach), transparent 70%),
      linear-gradient(100deg, var(--band-lilac) 0%, var(--band-lilac) 25%, var(--band-mist) 52%, var(--band-sky) 80%, var(--band-sky) 100%);
  }
  .person {
    position: absolute;
    left: 72px; top: 94px;
  }
  .person-name {
    font-weight: 600;
    font-size: 28px;
    line-height: 1.2;
    margin-bottom: 8px;
  }
  .address-line {
    font-size: 22px;
    line-height: 34px;
  }
  .divider {
    position: absolute;
    left: 546px; top: 54px;
    width: 9px; height: 194px;
    background: linear-gradient(180deg, var(--rule-green) 0%, var(--rule-purple) 40%, var(--rule-blue) 58%, var(--rule-orange) 100%);
  }
  .company {
    position: absolute;
    left: 620px; top: 44px;
  }
  .company-name {
    font-weight: 600;
    font-size: 29px;
    line-height: 1.2;
    margin-bottom: 8px;
  }
  .contact-line {
    font-size: 23px;
    line-height: 41px;
  }
</style>
</head>
<body>
  <main class="card">
    <div class="brand">
      <span class="brand-name">STEADYWAVE</span>
      <span class="brand-mark"></span>
    </div>
    <p class="job-title">General manager</p>

    <section class="info-band">
      <div class="person">
        <h1 class="person-name">DANIEL MORROW, p. ENG</h1>
        <p class="address-line">1280 Harbour Ln, Suite 204</p>
        <p class="address-line">Lakeview Ontario A1B 2C3, Canada</p>
      </div>

      <div class="divider"></div>

      <div class="company">
        <h2 class="company-name">STEADYWAVE INC</h2>
        <p class="contact-line">o.(555) 014- 2200 ext.201</p>
        <p class="contact-line">c. (555) 019- 3344</p>
        <p class="contact-line">e. dmorrow@steadywave.example,</p>
        <p class="contact-line">www.steadywave.example</p>
      </div>
    </section>
  </main>
</body>
</html>
```